Premium Lawn fertiliser packaging - Looking for long term designer

*Update at bottom
I need a carefully considered, bold and professional packaging design for my new premium lawn fertiliser product. This contest is for a detailed front of the stand-up pouch packaging and once I’ve chosen a winner, they’ll be asked to create the layout for the back that links to the front as well. I have a full range of additional products that will also need designs and so I'm looking for someone who can do a great job here and who we can work with long term.

The front should include our logo for Pemberly Turf Supply Direct and be titled “Bloom Vigor Max” "Professional Lawn Fertiliser". The spring fertiliser tag line is "Awaken your lawn: Lush Greening, Lasting Health".
Beneath it, it then needs to include some important usage information and the key benefits along with some suitable graphic.

Key information to include:

Apply March - June
Treats 35-50 m2
16-3-8
+2%MgO + 1% Fe + 2.9% CaO (this is the chemical makeup of the fertiliser and needs to be fairly prominent. If you look at other professional fertiliser packaging, you'll see how it needs to compare).

Key features:
Premium fertiliser, used by professionals
Advanced greening with micro-nutrient complex
Dual action Nitrogen: Instant green boost & continuous feed for 3 months
Child & pet safe

Our brand colours are purple and green. Purple = #592999, Green = 3cb64a / 81d742 / 4d9d44

I think these colours look great against a white background.

Please make sure you look at our website as well to get an idea of our brand: www.pemberlyturfsupply.co.uk

To help, I've attached images of competitors fertiliser packaging that I like the look of. I'm not looking for you to copy but just see what type of thing appeals to me, the standard I'm expecting and what I need to compete against....

In addition, I have also attached some potential images you may wish to try using in your design, although please feel free to use your own if you have something better. For the moment, the images are 'preview' images, but once I decide on a design and we agree on the correct image, I will download and send over a fully licensed version.

*** Update*** When submitting your design, can you submit it in 2 formats: The first as a fully printed custom stand-up pouch and the second as a full-size label stuck onto a standup pouch (whatever colour you think is right for your design - choose white if you are not sure). To explain, I've just discovered we won't be able to get full custom bags printed in time for the first run and so we will have to opt for the design to be printed on labels and fixed onto bags. I therefore need to choose a design that works in both formats as both a label on a standup pouch as well as a fully printed pouch. Many thanks.

Target Market(s)

Domestic home-owners

Industry/Entity Type

Lawn care. NOT AGRICULTURE OR FARMING

Font styles to use
Sans Serif

Requirements
Must have
• Presented in 2 formats - see update at bottom of description
Nice to have
• I quite like designs against a white background, although I’m open to other ideas as well.
Should not have
• Please do not include any people or faces in the design. The text should be solid in colour, so no graduated colour fill in the text or outline text. Please avoid over-busy or cluttered designs.

```html
<!DOCTYPE html>
<html lang="en">
<head>
<meta charset="UTF-8">
<title>Bloom Vigor Max – Pouch Front</title>
<link href="https://fonts.googleapis.com/css2?family=Poppins:wght@300;500;600;700;800&family=Quicksand:wght@400;500;700&display=swap" rel="stylesheet">
<style>
  :root {
    --purple: #592999;
    --purple-bright: #6230a8;
    --green-title: #62b03a;
    --green-band: #4d9d44;
    --green-light: #81d742;
    --green-dark: #2f5a14;
    --white: #ffffff;
    --grey-bg: #8f8f8f;
    --grey-box: #cdcdcd;
    --soil: #2b2b2b;
  }
  * { margin: 0; padding: 0; box-sizing: border-box; }
  html, body { width: 1200px; height: 720px; overflow: hidden; }
  body { background: var(--grey-bg); position: relative; font-family: "Poppins", sans-serif; }

  .pouch-front {
    position: absolute; left: 430px; top: 15px;
    width: 340px; height: 690px;
    background: var(--white); overflow: hidden;
  }

  .top-seal { position: absolute; left: 0; top: 0; width: 340px; height: 68px; }
  .top-seal-text {
    position: absolute; left: 0; top: 22px; width: 100%;
    text-align: center; color: var(--white);
    font-size: 10.5px; font-weight: 500; letter-spacing: 0.2px;
  }
  .top-seal-text strong { font-weight: 800; }

  .brand { position: absolute; top: 92px; left: 0; width: 100%; text-align: center; }
  .brand-dot { display: block; width: 34px; height: 34px; border-radius: 50%; background: var(--green-band); margin: 0 auto 8px; }
  .brand-name { color: var(--green-band); font-weight: 600; font-size: 16px; line-height: 1.2; letter-spacing: 0.5px; }

  .product-title {
    position: absolute; top: 200px; left: 0; width: 100%; text-align: center;
    color: var(--green-title); font-weight: 800; font-size: 46px;
    line-height: 48px; letter-spacing: -1px;
  }
  .product-sub {
    position: absolute; top: 300px; left: 0; width: 100%; text-align: center;
    color: var(--purple); font-weight: 600; font-size: 12.5px; letter-spacing: 0.3px;
  }

  .tagline {
    position: absolute; top: 334px; left: 32px; width: 276px; height: 52px;
    background: var(--purple-bright); border-radius: 7px; color: var(--white);
    text-align: center; padding-top: 7px;
  }
  .tagline-lead { font-weight: 300; font-size: 12px; line-height: 17px; }
  .tagline-main { font-weight: 600; font-size: 13px; line-height: 18px; }

  .benefit-band {
    position: absolute; top: 418px; left: 0; width: 250px; height: 104px;
    background: var(--green-band);
  }
  .benefits { list-style: none; position: absolute; left: 14px; top: 10px; width: 150px; }
  .benefits li {
    position: relative; padding-left: 11px; margin-bottom: 7px;
    color: var(--white); font-family: "Quicksand", sans-serif;
    font-size: 8.5px; line-height: 10px; font-weight: 500;
  }
  .benefits li::before { content: "\221A"; position: absolute; left: 0; top: 0; font-size: 9px; }
  .benefits li strong { font-weight: 700; }

  .turf-visual {
    position: absolute; top: 402px; left: 180px; width: 150px; height: 124px;
    background: linear-gradient(180deg, var(--green-light) 0%, #3f8f2a 62%, var(--soil) 62%, #161616 100%);
    border-radius: 4px;
  }

  .usage { position: absolute; top: 542px; left: 0; width: 100%; height: 50px; }
  .usage-col { position: absolute; top: 0; width: 150px; text-align: center; color: var(--green-dark); }
  .usage-col.treats { left: 20px; }
  .usage-col.apply { left: 172px; }
  .usage-label { font-weight: 300; font-size: 16px; line-height: 20px; }
  .usage-value { font-weight: 600; font-size: 16px; line-height: 22px; }
  .usage-divider { position: absolute; left: 170px; top: 0; width: 1px; height: 44px; background: var(--green-dark); }

  .formula {
    position: absolute; top: 608px; left: 18px; width: 200px; height: 50px;
    background: var(--grey-box); border-radius: 6px; text-align: center;
    color: var(--green-dark); font-weight: 600; font-size: 12.5px; line-height: 18px; padding-top: 7px;
  }

  .bottom-band { position: absolute; left: 0; bottom: 0; width: 340px; height: 90px; }
  .net-weight {
    position: absolute; right: 22px; bottom: 22px; color: var(--white);
    font-weight: 700; font-size: 30px; line-height: 30px;
  }
  .net-weight small { font-size: 12px; font-weight: 500; }
</style>
</head>
<body>
  <main class="pouch-front">
    <svg class="top-seal" viewBox="0 0 340 68" aria-hidden="true">
      <path d="M0,0 H340 V60 L334,66 L328,60 L322,66 L316,60 L310,66 L304,60 L298,66 L292,60 L286,66 L280,60 L274,66 L268,60 L262,66 L256,60 L250,66 L244,60 L238,66 L232,60 L226,66 L220,60 L214,66 L208,60 L202,66 L196,60 L190,66 L184,60 L178,66 L172,60 L166,66 L160,60 L154,66 L148,60 L142,66 L136,60 L130,66 L124,60 L118,66 L112,60 L106,66 L100,60 L94,66 L88,60 L82,66 L76,60 L70,66 L64,60 L58,66 L52,60 L46,66 L40,60 L34,66 L28,60 L22,66 L16,60 L10,66 L4,60 L0,64 Z" fill="#6230a8"/>
    </svg>
    <p class="top-seal-text"><strong>PREMIUM FERTILISER</strong>, USED BY PROFESSIONALS</p>

    <div class="brand">
      <span class="brand-dot"></span>
      <p class="brand-name">Pemberly Turf<br>Supply Direct</p>
    </div>

    <h1 class="product-title">BLOOM<br>VIGOR MAX</h1>
    <p class="product-sub">PROFESSIONAL LAWN FERTILISER</p>

    <div class="tagline">
      <p class="tagline-lead">AWAKEN YOUR LAWN:</p>
      <p class="tagline-main">LUSH GREENING, LASTING HEALTH</p>
    </div>

    <section class="benefit-band">
      <ul class="benefits">
        <li>Advanced greening with micro-nutrient complex.</li>
        <li><strong>Dual action Nitrogen:</strong> Instant green boost &amp; continuous feed for 3 months.</li>
        <li>Child &amp; pet safe</li>
      </ul>
    </section>
    <div class="turf-visual" role="img" aria-label="Square block of lush green lawn grass on dark soil"></div>

    <section class="usage">
      <div class="usage-col treats">
        <p class="usage-label">TREATS</p>
        <p class="usage-value">35-50 M2</p>
      </div>
      <span class="usage-divider"></span>
      <div class="usage-col apply">
        <p class="usage-label">APPLY</p>
        <p class="usage-value">MARCH - JUNE</p>
      </div>
    </section>

    <svg class="bottom-band" viewBox="0 0 340 90" aria-hidden="true">
      <path d="M0,72 H220 C250,72 245,22 285,22 H340 V90 H0 Z" fill="#6230a8"/>
    </svg>
    <div class="formula">16-3-8 +2 % MgO<br>+ 1 % Fe + 2,9 % CaO</div>
    <p class="net-weight">10<small>kg</small></p>
  </main>
</body>
</html>
```